Business Card Design

I need Business card designs with following on cards:

Dorian Felsk
Director

M: +61 491 208 356
D: +61 7 5580 1926
F: +61 7 5580 6471
E: dorian@mevrostrand.example.au

Mevro Group
Suite 4/61 North Calloway Road
Tindall Point QLD 4299

Ross Halvorn
Director

M: +61 438 902 615
D: +61 7 5580 1926
F: +61 7 5580 6471
E: ross@mevrostrand.example.au

Mevro Group
Tindall Point QLD 4299

Mevro Group Logo has been attached to brief.

Industry/Entity Type

Business

```html
<!DOCTYPE html>
<html lang="en">
<head>
<meta charset="utf-8">
<title>Mevro Group — Business Card</title>
<link rel="stylesheet" href="https://fonts.googleapis.com/css2?family=Open+Sans:ital,wght@0,400;0,600;0,700;1,400&display=swap">
<style>
  :root {
    --bg-light: #b9b9b9;
    --bg-dark: #3a3a3a;
    --orange: #f7941d;
    --orange-deep: #f08a12;
    --ink: #111111;
    --white: #ffffff;
    --rule: #f7a440;
  }
  * { box-sizing: border-box; margin: 0; padding: 0; }
  html, body { width: 1200px; height: 900px; overflow: hidden; }
  body {
    position: relative;
    background: radial-gradient(ellipse at 30% 30%, var(--bg-light) 0%, #8a8a8a 45%, var(--bg-dark) 100%);
    font-family: "Open Sans", "Segoe UI", sans-serif;
  }
  .card {
    position: absolute;
    width: 520px;
    height: 300px;
    box-shadow: 0 14px 30px rgba(0,0,0,.35);
    overflow: hidden;
  }
  .card--front {
    left: 110px; top: 130px;
    background: linear-gradient(180deg, var(--orange-deep) 0%, var(--orange) 100%);
    display: flex; align-items: center; justify-content: center;
  }
  .card--back {
    left: 570px; top: 460px;
    background: var(--white);
  }
  .brand {
    display: flex; align-items: center; gap: 12px;
    font-weight: 600;
    letter-spacing: 4px;
    text-transform: uppercase;
  }
  .brand__dot { border-radius: 50%; flex: none; }
  .card--front .brand { color: var(--white); font-size: 40px; }
  .card--front .brand__dot { width: 22px; height: 22px; background: var(--white); }
  .card--back .brand {
    position: absolute; left: 0; right: 0; top: 42px;
    justify-content: center;
    color: var(--ink); font-size: 28px;
  }
  .card--back .brand__dot { width: 16px; height: 16px; background: var(--orange); }
  .person { position: absolute; left: 30px; top: 112px; }
  .person__name { color: var(--orange); font-size: 19px; font-weight: 400; line-height: 1.1; }
  .person__role { color: var(--orange); font-size: 11px; font-style: italic; margin-top: 2px; }
  .rule {
    position: absolute; left: 28px; right: 40px; top: 160px;
    height: 1px; background: linear-gradient(90deg, var(--rule), rgba(247,164,64,0));
  }
  .contacts { position: absolute; left: 30px; top: 170px; list-style: none; }
  .contacts li { font-size: 12.5px; line-height: 18px; color: var(--ink); display: flex; }
  .contacts b { color: var(--orange); font-weight: 700; width: 26px; }
  .address-bar {
    position: absolute; left: 0; right: 0; bottom: 0; height: 26px;
    background: linear-gradient(90deg, var(--orange) 0%, var(--orange) 55%, rgba(247,148,29,0) 100%);
    color: var(--white); font-size: 11px; letter-spacing: .5px;
    text-transform: uppercase; padding-left: 14px; line-height: 26px;
  }
</style>
</head>
<body>
  <section class="card card--front" aria-label="Card front">
    <div class="brand"><span class="brand__dot"></span>Mevro Group</div>
  </section>

  <section class="card card--back" aria-label="Card back">
    <div class="brand"><span class="brand__dot"></span>Mevro Group</div>
    <div class="person">
      <p class="person__name">Dorian Felsk</p>
      <p class="person__role">Director</p>
    </div>
    <div class="rule"></div>
    <ul class="contacts">
      <li><b>M:</b>+61 491 208 356</li>
      <li><b>D:</b>+61 7 5580 1926</li>
      <li><b>F:</b>+61 7 5580 6471</li>
      <li><b>E:</b>dorian@mevrostrand.example.au</li>
    </ul>
    <div class="address-bar">Suite 4/61 North Calloway Road, Tindall Point QLD 4299</div>
  </section>
</body>
</html>
```